Birchline Heating & Air

I need a business card made for my company. I would like my new logo for Birchline Heating and Air on the front and my Garage Door on the back.
Front to say -Heating & Air Conditioning , Mini Splits and Heat Pumps, Hydronic In-Floor Heat. Locally Owned and Operated! Licensed, Boned and Insured. Free Estimates on new equipment. 715-408-2159
BGD Back Card, change phone# to 651-374-5810. Remove Commercial and residential and fully sticked vans lines.

```html
<!DOCTYPE html>
<html lang="en">
<head>
<meta charset="utf-8">
<title>Birchline Heating &amp; Air / Birchline Garage Door – Business Cards</title>
<link rel="stylesheet" href="https://fonts.googleapis.com/css2?family=Open+Sans:wght@400;600;700;800&family=Russo+One&display=swap">
<style>
  :root {
    --backdrop: #232323;
    --card-cream: #fdfdf6;
    --fold-grey: #d6d6d6;
    --brand-red: #e8202a;
    --brand-red-deep: #b3141c;
    --brand-blue: #1c5a9c;
    --ink: #111111;
    --white: #ffffff;
  }
  * { box-sizing: border-box; margin: 0; padding: 0; }
  html, body {
    width: 1200px; height: 780px; overflow: hidden;
    background: var(--backdrop);
  }
  .stage {
    position: relative; width: 1200px; height: 780px;
    display: flex; justify-content: center; align-items: center; gap: 60px;
  }
  .card {
    position: relative; width: 340px; height: 595px;
    border-radius: 26px; overflow: hidden;
    background: var(--card-cream);
    box-shadow: 0 14px 30px rgba(0,0,0,.55);
    font-family: "Open Sans", Arial, sans-serif;
    color: var(--ink);
  }
  .card-backdrop { position: absolute; inset: 0; width: 100%; height: 100%; }
  .card-content {
    position: relative; z-index: 1;
    display: flex; flex-direction: column; align-items: center;
    text-align: center; padding: 38px 22px 0;
  }
  .brand-name {
    display: flex; align-items: center; gap: 10px;
    font-family: "Open Sans", Arial, sans-serif;
    font-weight: 800; font-size: 27px; line-height: 1.05;
    color: var(--brand-blue);
  }
  .brand-dot {
    flex: none; width: 18px; height: 18px; border-radius: 50%;
    background: var(--brand-red);
  }
  .brand-rule {
    width: 230px; height: 2px; margin-top: 10px;
    background: var(--brand-red);
  }
  .save-line {
    margin-top: 20px;
    font-family: "Russo One", "Arial Black", sans-serif;
    font-size: 25px; letter-spacing: 1px;
    color: var(--brand-red);
  }
  .phone {
    font-weight: 700; font-size: 27px; line-height: 1.15; letter-spacing: .5px;
  }
  .email { font-size: 14px; font-weight: 600; margin-top: 2px; }
  .service-list {
    list-style: none; margin-top: 16px;
    font-size: 14.5px; font-weight: 600; line-height: 1.4;
  }
  .service-list li::before { content: "• "; }
  .offer-badge {
    position: relative; width: 220px; height: 110px; margin-top: 10px;
    transform: rotate(-12deg);
  }
  .offer-badge svg { position: absolute; inset: 0; width: 100%; height: 100%; }
  .offer-text {
    position: absolute; inset: 0;
    display: flex; flex-direction: column; justify-content: center; align-items: center;
    color: var(--white); line-height: 1.05;
  }
  .offer-headline {
    font-family: "Russo One", "Arial Black", sans-serif;
    font-size: 29px; letter-spacing: 1px;
  }
  .offer-sub { font-weight: 600; font-size: 13.5px; }
  .offer-sub--caps { font-family: "Russo One", "Arial Black", sans-serif; font-size: 16px; font-weight: 400; }
  .website-block {
    position: absolute; z-index: 1; left: 0; right: 0; bottom: 52px;
    text-align: center; color: var(--white); white-space: nowrap;
    transform: rotate(-15deg); transform-origin: center;
  }
  .website-label { font-size: 14px; font-weight: 600; }
  .website-url { font-size: 15px; font-weight: 600; line-height: 1.2; }
  .website-url strong { font-size: 21px; font-weight: 600; }
</style>
</head>
<body>
<main class="stage">

  <!-- Front: heating & air -->
  <article class="card card--heating">
    <svg class="card-backdrop" viewBox="0 0 340 595" preserveAspectRatio="none" aria-hidden="true">
      <defs>
        <linearGradient id="redBandA" x1="0" y1="0" x2="1" y2="1">
          <stop offset="0" stop-color="var(--brand-red-deep)"/>
          <stop offset=".45" stop-color="var(--brand-red)"/>
        </linearGradient>
        <linearGradient id="foldA" x1="0" y1="0" x2="0" y2="1">
          <stop offset="0" stop-color="var(--fold-grey)"/>
          <stop offset="1" stop-color="#ffffff"/>
        </linearGradient>
        <filter id="curlShadowA" x="-10%" y="-10%" width="120%" height="130%">
          <feDropShadow dx="0" dy="6" stdDeviation="6" flood-color="#000" flood-opacity=".25"/>
        </filter>
      </defs>
      <path d="M0 500 L340 410 L340 595 L0 595 Z" fill="url(#redBandA)"/>
      <path d="M0 440 Q210 450 340 330 L340 410 L0 500 Z" fill="url(#foldA)"/>
      <path d="M0 0 H340 V330 Q280 440 40 448 L0 448 Z" fill="var(--card-cream)" filter="url(#curlShadowA)"/>
    </svg>
    <div class="card-content">
      <div class="brand-name"><span class="brand-dot"></span><span>Birchline<br>Heating &amp; Air</span></div>
      <p class="save-line">SAVE THIS CARD!</p>
      <p class="phone">715-408-2159</p>
      <p class="email">hello@birchlinegaragedoor.com</p>
      <ul class="service-list">
        <li>Boned and Insured</li>
        <li>Hydronic In-Floor Heat</li>
        <li>Heating &amp; Air Conditioning</li>
        <li>Mini Splits and Heat Pumps</li>
        <li>Locally Owned and Operated! Licensed</li>
      </ul>
      <div class="offer-badge">
        <svg viewBox="0 0 260 130" aria-hidden="true">
          <polygon fill="var(--brand-red)" stroke="var(--brand-blue)" stroke-width="2.5" stroke-linejoin="miter"
            points="255,65 220.3,78 231.1,100.3 185.9,99 168.6,122.1 130,107 91.4,122.1 74.1,99 28.9,100.3 39.7,78 5,65 39.7,52 28.9,29.7 74.1,31 91.4,7.9 130,23 168.6,7.9 185.9,31 231.1,29.7 220.3,52"/>
        </svg>
        <div class="offer-text">
          <span class="offer-headline">FREE</span>
          <span class="offer-sub">Estimates on</span>
          <span class="offer-sub">new equipment</span>
        </div>
      </div>
    </div>
    <div class="website-block">
      <p class="website-label">Visit Our Website:</p>
      <p class="website-url">www.<strong>BirchlineGarage</strong> Door.com</p>
    </div>
  </article>

  <!-- Back: garage door -->
  <article class="card card--garage">
    <svg class="card-backdrop" viewBox="0 0 340 595" preserveAspectRatio="none" aria-hidden="true">
      <defs>
        <linearGradient id="redBandB" x1="0" y1="0" x2="1" y2="1">
          <stop offset="0" stop-color="var(--brand-red-deep)"/>
          <stop offset=".45" stop-color="var(--brand-red)"/>
        </linearGradient>
        <linearGradient id="foldB" x1="0" y1="0" x2="0" y2="1">
          <stop offset="0" stop-color="var(--fold-grey)"/>
          <stop offset="1" stop-color="#ffffff"/>
        </linearGradient>
        <filter id="curlShadowB" x="-10%" y="-10%" width="120%" height="130%">
          <feDropShadow dx="0" dy="6" stdDeviation="6" flood-color="#000" flood-opacity=".25"/>
        </filter>
      </defs>
      <path d="M0 500 L340 410 L340 595 L0 595 Z" fill="url(#redBandB)"/>
      <path d="M0 440 Q210 450 340 330 L340 410 L0 500 Z" fill="url(#foldB)"/>
      <path d="M0 0 H340 V330 Q280 440 40 448 L0 448 Z" fill="var(--card-cream)" filter="url(#curlShadowB)"/>
    </svg>
    <div class="card-content">
      <div class="brand-name"><span class="brand-dot"></span><span>Birchline<br>Garage Door</span></div>
      <div class="brand-rule"></div>
      <p class="save-line">SAVE THIS CARD!</p>
      <p class="phone">651-374-5810</p>
      <p class="email">hello@birchlinegaragedoor.com</p>
      <ul class="service-list">
        <li>Same Day &amp; Emergency Service</li>
        <li>Locally Owned &amp; Operated</li>
        <li>All Major Brands</li>
      </ul>
      <div class="offer-badge">
        <svg viewBox="0 0 260 130" aria-hidden="true">
          <polygon fill="var(--brand-red)" stroke="var(--brand-blue)" stroke-width="2.5" stroke-linejoin="miter"
            points="255,65 220.3,78 231.1,100.3 185.9,99 168.6,122.1 130,107 91.4,122.1 74.1,99 28.9,100.3 39.7,78 5,65 39.7,52 28.9,29.7 74.1,31 91.4,7.9 130,23 168.6,7.9 185.9,31 231.1,29.7 220.3,52"/>
        </svg>
        <div class="offer-text">
          <span class="offer-headline">FREE</span>
          <span class="offer-sub offer-sub--caps">SERVICE CALL</span>
        </div>
      </div>
    </div>
    <div class="website-block">
      <p class="website-label">Visit Our Website:</p>
      <p class="website-url">www.<strong>BirchlineGarage</strong> Door.com</p>
    </div>
  </article>

</main>
</body>
</html>
```